Wedding Invitation and envelope package

I need the 1st of many invitation designs. This is a floral collection and I have attached many designs that I like from competitors. I think that the pastel look is the best but I am hoping you can make something special. The font selection is just as important as the imagery. The overall size with bleeds is 5.25 x 7.25" and I have attached a sample to make sure sizing is clear. I also need A7 envelopes to go with the invitation, front and back flap. I want someone to look at the design and say they would pick it over any of the samples. I will need 8 total floral designs done over the next few weeks after this 1st one is done. I will also need a collection of 8 modern designs done. Please ask any questions

Font styles to use
Serif
Sans Serif
Script

Requirements
Must have
• This is a single sided invitation, a back side is not needed.
Should not have
• No full solid dark backgrounds

```html
<!DOCTYPE html>
<html lang="en">
<head>
<meta charset="utf-8">
<title>Wildflower Wedding Suite</title>
<link href="https://fonts.googleapis.com/css2?family=Sacramento&family=Montserrat:wght@400;500&family=Playfair+Display:wght@700&display=swap" rel="stylesheet">
<style>
  :root {
    --backdrop: #c5d2da;
    --paper: #fcf4ef;
    --paper-white: #fdfaf7;
    --ink: #3c3c3c;
    --rule: #c9bdb6;
    --gold: #f6c75a;
    --gold-soft: #fbd97f;
    --navy: #3d5580;
    --sage: #9fb08a;
    --rose: #d9a3ad;
    --slate: #7f98ad;
  }
  * { margin: 0; padding: 0; box-sizing: border-box; }
  html, body { width: 1200px; height: 890px; overflow: hidden; }
  body { background: var(--backdrop); position: relative; font-family: "Montserrat", sans-serif; color: var(--ink); }
  .piece { position: absolute; background: var(--paper); }
  .script { font-family: "Sacramento", cursive; font-weight: 400; line-height: 1; white-space: nowrap; }
  .caps { text-transform: uppercase; letter-spacing: 0.04em; }

  /* Cover card */
  .cover-card { left: 89px; top: 86px; width: 267px; height: 374px; }
  .cover-card .wreath {
    position: absolute; left: 2px; top: 14px; width: 263px; height: 330px; border-radius: 50%;
    background:
      radial-gradient(ellipse at center, var(--paper) 0 52%, transparent 60%),
      conic-gradient(from 20deg, var(--slate), var(--gold-soft), var(--sage), var(--rose), var(--navy), var(--sage), var(--gold-soft), var(--rose), var(--slate));
    opacity: 0.75;
  }
  .monogram { position: absolute; left: 0; right: 0; top: 118px; display: flex; justify-content: center; align-items: center; gap: 4px; }
  .monogram .initial { font-size: 104px; color: var(--ink); }
  .ampersand-badge {
    width: 34px; height: 34px; border-radius: 50%; background: var(--gold-soft);
    display: flex; align-items: center; justify-content: center;
    font-family: "Playfair Display", serif; font-weight: 700; font-size: 20px; color: var(--ink);
  }

  /* Invitation card */
  .invitation { left: 397px; top: 85px; width: 267px; height: 374px; overflow: hidden;
    background: linear-gradient(135deg, #e6ecf2, #f7efe6 30%, #eef0e4 55%, #f6e6e8 80%, #e4eaf1); }
  .invitation .floral-border { position: absolute; inset: 0; background: inherit; }
  .invitation .panel {
    position: absolute; left: 43px; top: 42px; width: 181px; height: 291px;
    background: var(--paper); border: 1px solid var(--rule);
    text-align: center; padding-top: 12px;
  }
  .couple-name { font-size: 28px; color: var(--ink); }
  .small-badge {
    width: 18px; height: 18px; border-radius: 50%; background: #4a4a4a; margin: 0 auto 0;
    display: flex; align-items: center; justify-content: center;
    font-family: "Playfair Display", serif; font-weight: 700; font-size: 11px; color: var(--gold);
  }
  .fine { font-size: 5.4px; line-height: 1.55; }
  .guests { font-size: 22px; margin: 8px 0 10px; }
  .day { font-size: 7.5px; margin-top: 7px; letter-spacing: 0.05em; }
  .date { font-size: 12px; font-weight: 500; letter-spacing: 0.05em; margin: 1px 0 1px; }
  .time { font-size: 7px; margin-bottom: 8px; }
  .sign-off { font-size: 20px; margin-top: 8px; }

  /* Open envelope with liner */
  .open-envelope { position: absolute; left: 707px; top: 132px; width: 392px; height: 417px; }

  /* Envelope front */
  .envelope-front { left: 89px; top: 508px; width: 392px; height: 264px; }
  .recipient { position: absolute; left: 96px; top: 114px; width: 190px; text-align: center; }
  .recipient .name { font-size: 34px; }
  .recipient .address { font-size: 7.3px; line-height: 1.3; margin-top: 8px; letter-spacing: 0.05em; }
  .stem-flower {
    position: absolute; left: 294px; top: 110px; width: 12px; height: 80px; border-radius: 6px 6px 2px 2px;
    background: linear-gradient(180deg, var(--gold) 0 35%, #b9b48c 45%, #c6c29a 100%);
  }

  /* Envelope back */
  .envelope-back { left: 508px; top: 507px; width: 392px; height: 265px; background: var(--paper-white); }
  .envelope-back svg { position: absolute; inset: 0; }
  .return-block { position: absolute; left: 0; right: 0; top: 42px; text-align: center; }
  .return-block .name { font-size: 27px; }
  .return-block .address { font-size: 5.4px; line-height: 1.5; margin-top: 8px; }
</style>
</head>
<body>

  <section class="piece cover-card">
    <div class="wreath" role="img" aria-label="Watercolour wildflower wreath in blue, sage, rose and yellow"></div>
    <div class="monogram">
      <span class="initial script">C</span>
      <span class="ampersand-badge">&amp;</span>
      <span class="initial script">J</span>
    </div>
  </section>

  <section class="piece invitation">
    <div class="floral-border" role="img" aria-label="Scattered watercolour wildflower pattern border"></div>
    <div class="panel">
      <p class="couple-name script">Thomas Reed</p>
      <div class="small-badge">&amp;</div>
      <p class="couple-name script">Eleanor Hart</p>
      <p class="fine caps" style="margin-top:14px">Request the company of</p>
      <p class="guests script">Clara &amp; James</p>
      <p class="fine caps">To join them to celebrate their marrige<br>at an evening reception</p>
      <p class="day caps">Saturday</p>
      <p class="date">01.07.20</p>
      <p class="time">7.30PM</p>
      <p class="fine caps">At Linden Hall, Ashbury Green,<br>Meadow Lane, Wiltshire,<br>SN7 4QX</p>
      <p class="sign-off script">Carriages at midnight</p>
    </div>
  </section>

  <svg class="open-envelope" viewBox="0 0 392 417">
    <defs>
      <linearGradient id="liner-tones" x1="0" y1="0" x2="1" y2="1">
        <stop offset="0" stop-color="#f1f1ea"/>
        <stop offset="0.35" stop-color="#e4ead9"/>
        <stop offset="0.65" stop-color="#e6ebf1"/>
        <stop offset="1" stop-color="#f3e6e6"/>
      </linearGradient>
    </defs>
    <path d="M0 153 L180 8 Q196 -4 212 8 L392 153 L392 417 L0 417 Z" fill="var(--paper-white)"/>
    <path d="M25 153 L190 28 Q196 24 202 28 L367 153 L367 235 L25 235 Z" fill="url(#liner-tones)" role="img" aria-label="Watercolour wildflower envelope liner pattern"/>
    <path d="M0 153 L0 417 L196 260 Z" fill="#fbf6f2"/>
    <path d="M392 153 L392 417 L196 260 Z" fill="#faf4ef"/>
    <path d="M0 417 L185 270 Q196 261 207 270 L392 417 Z" fill="#fdfaf8"/>
  </svg>

  <section class="piece envelope-front">
    <div class="recipient">
      <p class="name script">Clara &amp; James</p>
      <p class="address caps">27 Willow Bank Road<br>Fairhaven, CT 06512</p>
    </div>
    <div class="stem-flower" role="img" aria-label="Small watercolour yellow wildflower"></div>
  </section>

  <section class="piece envelope-back">
    <svg viewBox="0 0 392 265" aria-hidden="true">
      <path d="M0 0 L392 0 L210 146 Q200 154 190 146 Z" fill="var(--paper)"/>
      <path d="M0 265 L190 146 Q200 140 210 146 L392 265 Z" fill="#fefcfa"/>
      <path d="M0 0 L0 265 L160 160 Z" fill="#fbf7f3"/>
      <path d="M392 0 L392 265 L240 160 Z" fill="#faf5f1"/>
    </svg>
    <div class="return-block">
      <p class="name script">Eleanor &amp; Thomas</p>
      <p class="address caps">At Linden Hall, Ashbury Green,<br>Meadow Lane, Wiltshire,<br>SN7 4QX</p>
    </div>
  </section>

</body>
</html>
```